New modern website for Kerbline Groundworks

Hi we are an existing company that has a current website http://www.kerblinegroundworks.co.nz/ we are looking to get a new vibrant looking website designed to take us further and gain more customers. We are after a simple easy to use website that does not confuse but we want to make an impact and stand out from the rest

Target Market(s)

Homeowners And Commercial Businesses

Industry/Entity Type

It Company

Coding

Coded - Design and coding required

Number of Pages Required

2 page

```html
<!DOCTYPE html>
<html lang="en">
<head>
<meta charset="utf-8">
<title>Kerbline Groundworks</title>
<link rel="stylesheet" href="https://fonts.googleapis.com/css2?family=Roboto:wght@300;400;700&display=swap">
<style>
:root{
  --amber:#f2a51f;
  --white:#ffffff;
  --ink:#444444;
  --crimson:#a01414;
  --red:#d3263a;
  --red-deep:#b81c2f;
  --sky:#1a96e8;
  --charcoal:#1f1f1f;
  --night:#161616;
  --yellow:#f2d11c;
  --blue:#1164b0;
  --blue-deep:#0b4f93;
}
*{margin:0;padding:0;box-sizing:border-box}
html,body{width:1200px;height:2723px;overflow:hidden}
body{position:relative;font-family:'Roboto',Arial,sans-serif;font-weight:300;background:var(--white);color:var(--white)}
.abs{position:absolute}

/* hero */
.hero{left:0;top:0;width:1200px;height:612px;background:linear-gradient(180deg,#4a4d52 0%,#3a3b3e 45%,#2a2a2b 100%)}
.hero-shade{left:0;top:0;width:1200px;height:612px;background:rgba(20,20,20,.35)}
.brand{left:0;top:205px;width:1200px;text-align:center;font-size:32px;font-weight:700;letter-spacing:1px;color:var(--white)}
.nav{left:0;top:268px;width:1200px;display:flex;justify-content:center;gap:62px;font-size:13px;font-weight:400;list-style:none}
.nav li::before{content:"+ ";font-weight:700}
.hero-title{left:0;top:300px;width:1200px;text-align:center;font-size:74px;font-weight:300;color:var(--amber);line-height:1.2}
.hero-sub{left:0;top:380px;width:1200px;text-align:center;font-size:30px;font-weight:300}
.dots{left:563px;top:468px;display:flex;gap:4px}
.dots span{width:16px;height:8px;border-radius:2px;background:var(--white)}
.dots span:first-child{background:var(--amber)}

/* intro */
.intro-title{left:0;top:680px;width:1200px;text-align:center;font-size:30px;color:var(--ink)}
.tile{width:300px;height:232px;padding:30px 26px;text-align:center}
.tile h3{font-weight:300;font-size:29px;margin-bottom:12px}
.tile p{font-size:11.5px;line-height:1.45;font-weight:400}
.tile-expertise{left:150px;top:762px;background:var(--crimson)}
.tile-services{left:750px;top:762px;background:var(--charcoal)}
.tile-concrete{left:450px;top:994px;background:var(--sky);padding-top:48px}
.tile-concrete h3{font-size:21px}
.photo-driveway{left:450px;top:762px;background:linear-gradient(180deg,#4c6b3a 0%,#6f7f63 50%,#9a9a96 100%)}
.photo-fleet{left:150px;top:994px;background:linear-gradient(180deg,#b7b9bd 0%,#a94040 55%,#8c8c8c 100%)}
.photo-crew{left:750px;top:994px;background:linear-gradient(180deg,#c8cbd0 0%,#8e8f90 55%,#6d6d6d 100%)}
.toggle{width:42px;height:42px}

/* services */
.services{left:0;top:1307px;width:1200px;height:508px;background:linear-gradient(90deg,var(--red-deep) 0%,var(--red) 60%,#e04556 100%)}
.services-title{left:166px;top:1450px;font-size:70px;font-weight:700;line-height:1}
.services-sub{left:150px;top:1520px;width:340px;text-align:center;font-size:30px;line-height:1.2}
.chevrons{left:505px;top:1500px}
.btn{display:flex;align-items:center;justify-content:center;gap:8px;font-size:15px;font-weight:400}
.btn-light{left:252px;top:1614px;width:136px;height:43px;background:var(--white);color:#222}
.photo-truck{left:563px;top:1398px;width:490px;height:300px;border-radius:10px;background:linear-gradient(160deg,#e8e8e8 0%,#c92a35 45%,#9b1e28 100%)}

/* projects */
.projects{left:0;top:1815px;width:1200px;height:505px;background:var(--night)}
.photo-home{left:191px;top:1879px;width:379px;height:379px;background:linear-gradient(180deg,#6a7a55 0%,#4a5440 45%,#2f3132 100%)}
.photo-path{left:581px;top:2111px;width:201px;height:147px;background:linear-gradient(180deg,#6f8a5a 0%,#8f9289 100%)}
.photo-paving{left:795px;top:2111px;width:203px;height:147px;background:linear-gradient(180deg,#9fb5a8 0%,#9a6a4c 60%,#8a5a40 100%)}
.projects-title{left:570px;top:1878px;width:458px;text-align:center;font-size:70px;font-weight:700;color:var(--sky);line-height:1}
.projects-sub{left:570px;top:1942px;width:458px;text-align:center;font-size:30px;line-height:1.22}
.btn-yellow{left:724px;top:2026px;width:138px;height:43px;background:var(--yellow);color:#333}

/* footer */
.footer{left:0;top:2320px;width:1200px;height:403px;background:linear-gradient(180deg,var(--blue) 0%,var(--blue-deep) 100%)}
.foot-head{font-size:21px;font-weight:300;opacity:.9}
.sitemap{left:150px;top:2410px}
.sitemap ul{list-style:none;margin-top:14px}
.sitemap li{font-size:11px;font-weight:400;margin-bottom:22px}
.locations{left:387px;top:2410px;width:230px;font-size:11px;font-weight:400;line-height:1.45}
.locations h4{font-size:11px;font-weight:700;margin-top:12px}
.locations .foot-head{margin-bottom:14px}
.newsletter{left:648px;top:2410px}
.email{left:650px;top:2447px;width:400px;height:38px;border:1px solid #cfe3f5;font-size:11px;padding:11px 8px;font-weight:400}
.subscribe{left:913px;top:2492px;width:137px;height:38px;background:#0a3e73;font-size:17px;font-weight:400;display:flex;align-items:center;justify-content:center}
.copyright{left:650px;top:2558px;width:400px;text-align:right;font-size:11px;font-weight:400}
</style>
</head>
<body>

<section>
  <div class="abs hero" role="img" aria-label="Photo of a depot yard with trucks and a concrete mixer"></div>
  <div class="abs hero-shade"></div>
  <div class="abs brand">Kerbline Groundworks</div>
  <ul class="abs nav"><li>HOME</li><li>ABOUT</li><li>SERVICES</li><li>PROJECTS</li><li>CONTACT US</li></ul>
  <h1 class="abs hero-title">Your one-stop specialist</h1>
  <p class="abs hero-sub">for driveway construction in Auckland</p>
  <div class="abs dots"><span></span><span></span><span></span><span></span></div>
</section>

<section>
  <h2 class="abs intro-title">The trusted name for all Concrete &amp; Asphalt Paving in Auckland</h2>

  <div class="abs tile tile-expertise">
    <h3>Our expertise</h3>
    <p>We have a reputation with clients in and around Auckland for achieving great results on time and within budget every time. We are proud to share our years of experience.</p>
  </div>
  <div class="abs tile photo-driveway" role="img" aria-label="Photo of a finished garden driveway"></div>
  <div class="abs tile tile-services">
    <h3>Additional Services</h3>
    <p>As part of our asphalt services, we are proud to offer a range of related services to our clients in the eastern suburbs and greater Auckland. Specialising in residential, commercial and industrial projects.</p>
  </div>
  <div class="abs tile photo-fleet" role="img" aria-label="Photo of the red company fleet with a seventy years experience seal"></div>
  <div class="abs tile tile-concrete">
    <h3>Concreting &amp; Asphalt Work</h3>
    <p>When it comes to all asphalt services, you can rest assured we will work around your schedule, requirements and budget. Servicing throughout Auckland, we specialise in.</p>
  </div>
  <div class="abs tile photo-crew" role="img" aria-label="Photo of a crew laying concrete"></div>

  <svg class="abs toggle" style="left:279px;top:973px" viewBox="0 0 42 42"><circle cx="21" cy="21" r="19" fill="none" stroke="#fff" stroke-width="2"/><path d="M13 18l8 8 8-8" fill="none" stroke="#fff" stroke-width="2"/></svg>
  <svg class="abs toggle" style="left:579px;top:973px" viewBox="0 0 42 42"><circle cx="21" cy="21" r="19" fill="none" stroke="#fff" stroke-width="2"/><path d="M13 25l8-8 8 8" fill="none" stroke="#fff" stroke-width="2"/></svg>
  <svg class="abs toggle" style="left:879px;top:973px" viewBox="0 0 42 42"><circle cx="21" cy="21" r="19" fill="none" stroke="#fff" stroke-width="2"/><path d="M13 18l8 8 8-8" fill="none" stroke="#fff" stroke-width="2"/></svg>
</section>

<section>
  <div class="abs services" role="img" aria-label="Red-tinted street scene with traffic cones"></div>
  <div class="abs photo-truck" role="img" aria-label="Photo of a red flatbed truck carrying a road roller"></div>
  <h2 class="abs services-title">SERVICES</h2>
  <p class="abs services-sub">Complete asphalt services for your next</p>
  <svg class="abs chevrons" width="48" height="80" viewBox="0 0 48 80"><path d="M4 4l20 36-20 36M16 4l20 36-20 36M28 4l16 36-16 36" fill="none" stroke="#fff" stroke-width="3"/></svg>
  <div class="abs btn btn-light">VIEW ALL <svg width="10" height="12" viewBox="0 0 10 12"><path d="M1 1l4 5-4 5M5 1l4 5-4 5" fill="none" stroke="#333" stroke-width="1.5"/></svg></div>
</section>

<section>
  <div class="abs projects"></div>
  <div class="abs photo-home" role="img" aria-label="Photo of a new asphalt driveway in front of a house"></div>
  <h2 class="abs projects-title">PROJECTS</h2>
  <p class="abs projects-sub">For residential driveways and commercial</p>
  <div class="abs btn btn-yellow">VIEW ALL <svg width="10" height="12" viewBox="0 0 10 12"><path d="M1 1l4 5-4 5M5 1l4 5-4 5" fill="none" stroke="#333" stroke-width="1.5"/></svg></div>
  <div class="abs photo-path" role="img" aria-label="Photo of a paved garden path"></div>
  <div class="abs photo-paving" role="img" aria-label="Photo of a red chip paved driveway"></div>
</section>

<footer>
  <div class="abs footer" role="img" aria-label="Blue-tinted photo of parked work trucks"></div>
  <div class="abs sitemap">
    <div class="foot-head">SITE MAP</div>
    <ul><li>HOME</li><li>ABOUT</li><li>SERVICES</li><li>PROJECTS</li><li>CONTACT US</li></ul>
  </div>
  <div class="abs locations">
    <div class="foot-head">LOCATIONS</div>
    <p>Kerbline Groundworks Ltd. 42 Harbour View Road, Penrose, AK 1061</p>
    <h4>PHONES:</h4>
    <p>800-5550-1234<br>800-5550-1235</p>
    <h4>E-MAIL:</h4>
    <p>hello@kerblinegroundworks.co.nz</p>
  </div>
  <div class="abs newsletter foot-head">NEWSLETTER SIGN UP</div>
  <div class="abs email">Email Id :</div>
  <div class="abs subscribe">Subscribe</div>
  <p class="abs copyright">© 2016 Kerbline Groundworks All Rights Reserved.</p>
</footer>

</body>
</html>
```